Homepage design for female-owned English/French speaking Law firm

Brief Update - we prefer not to have a photo of a person in the hero shot

Morlewy.com.au is the website for a English/French Bilingual Female-owned Law Firm, Quillomette Morlewy.
Overall Design notes:
Professional, yet warm and welcoming
Historic foundations but Progressive, woman-owned, sleek, innovative and modern.
Approachable, casual yet professional. Sans-serif font and light colours would help this
2 languages switched by flags (English/French)

Winner must provide
Home page design
Standard (inner) page design (can be provided after winner is selected)
All photos used in the design without charge

Number of Pages Required

2 page

Requirements
Should not have
• Update - we prefer not to have a photo of a person in the hero shot

```html
<!DOCTYPE html>
<html lang="en">
<head>
<meta charset="utf-8">
<title>Quillomette Morlewy Solicitors</title>
<link href="https://fonts.googleapis.com/css2?family=Poppins:wght@400;500;600;700&family=Roboto:wght@400;500&family=Tinos&display=swap" rel="stylesheet">
<style>
:root{
  --green:#43624f;
  --mint:#9ccfb0;
  --grey-bg:#ebebeb;
  --grey-top:#9a9a9a;
  --text:#6b6b6b;
  --ink:#1f2a2a;
  --footer:#1e1e1e;
  --white:#ffffff;
}
*{margin:0;padding:0;box-sizing:border-box}
html,body{width:1200px;height:3469px;overflow:hidden;background:var(--white)}
body{position:relative;font-family:"Roboto",sans-serif;color:var(--text)}
.abs{position:absolute}

/* header */
.topbar{left:375px;top:0;width:825px;height:43px;background:var(--grey-top);clip-path:polygon(30px 0,100% 0,100% 100%,0 100%)}
.topbar-item{top:9px;color:#fff;font-size:15px;display:flex;align-items:center;gap:12px}
.topbar-item .ico{width:26px;height:26px;border:2px solid #fff;border-radius:50%;display:flex;align-items:center;justify-content:center}
.quote-btn{left:915px;top:0;width:285px;height:43px;background:var(--green);clip-path:polygon(0 0,100% 0,100% 100%,30px 100%);color:#fff;font:600 15px "Poppins",sans-serif;display:flex;align-items:center;justify-content:center;padding-left:20px}
.brand{left:112px;top:20px;display:flex;align-items:center;gap:10px;color:var(--green);font:600 16px/1.25 "Poppins",sans-serif}
.brand-mark{width:60px;height:60px;border:5px solid var(--green);border-radius:50%;flex:none}
.nav{top:69px;left:521px;display:flex;gap:34px;font:500 15px "Roboto",sans-serif;color:var(--ink)}
.lang{left:998px;top:68px;display:flex;align-items:center;gap:8px;font:600 16px "Tinos",serif;color:var(--green)}
.flag{width:22px;height:22px;border-radius:50%;background:linear-gradient(135deg,#1b3a8c 50%,#c8202f 50%)}

/* hero */
.hero{left:0;top:106px;width:1200px;height:643px;background:linear-gradient(180deg,#6e5d66 0%,#8d6a5b 35%,#3d4c55 60%,#28394a 100%)}
.hero-band{left:0;top:706px;width:1200px;height:43px;background:var(--green);clip-path:polygon(0 100%,100% 0,100% 100%)}
.hero-title{left:0;width:1200px;top:296px;text-align:center;color:#fff;font:600 52px/1.15 "Poppins",sans-serif}
.hero-text{left:0;width:1200px;top:434px;text-align:center;color:#fff;font:15.5px/1.6 "Tinos",serif}
.btn{background:var(--green);color:#fff;display:flex;align-items:center;justify-content:center;font:500 16px "Poppins",sans-serif}
.hero-btn{left:492px;top:501px;width:216px;height:46px;letter-spacing:.3px}
.dots{left:560px;top:648px;display:flex;gap:12px}
.dots span{width:14px;height:14px;border-radius:50%;background:#fff}
.dots span.off{background:transparent;border:2px solid var(--mint)}

/* about */
.about-deco{left:105px;top:918px;width:76px;height:76px;border-radius:50%;background:#9c9c9c}
.about-ring{left:107px;top:848px;width:480px;height:480px;border-radius:50%;background:var(--mint)}
.about-photo{left:119px;top:855px;width:468px;height:468px;border-radius:50%;background:linear-gradient(135deg,#e9ecef,#bfc7cf 60%,#6d6a5a)}
.about-portrait{left:397px;top:1179px;width:150px;height:150px;border-radius:50%;border:4px solid #3c3c3c;background:linear-gradient(160deg,#b46a3a,#e7c2a5)}
.about-body{left:630px;top:865px;width:464px}
.about-body h2{font:600 35px "Poppins",sans-serif;color:var(--ink);margin-bottom:14px}
.about-body p{font:15px/1.78 "Roboto",sans-serif;text-align:justify}
.about-body ul{list-style:none;margin:14px 0 12px}
.about-body li{display:flex;gap:14px;font:15px/1.75 "Roboto",sans-serif;margin-bottom:12px;padding-right:40px}
.about-body li:before{content:"";flex:none;width:12px;height:12px;margin-top:7px;border:2px solid var(--green);border-radius:50%;box-shadow:inset 0 0 0 2px #fff,inset 0 0 0 6px var(--green)}
.about-btn{position:relative;margin-top:22px;width:165px;height:46px}

/* services */
.services{left:0;top:1432px;width:1200px;height:629px;background:var(--grey-bg)}
.services-band{left:0;top:2016px;width:1200px;height:48px;background:var(--green);clip-path:polygon(0 0,100% 95%,100% 100%,0 100%)}
.eyebrow{left:0;width:1200px;text-align:center;color:var(--green);font:600 18px "Poppins",sans-serif;letter-spacing:.5px}
.section-title{left:0;width:1200px;text-align:center;color:var(--ink);font:600 29px "Poppins",sans-serif;letter-spacing:.5px}
.service{top:1636px;width:232px}
.service-head{display:flex;gap:12px;align-items:center;height:64px;border-bottom:1px solid #d9d9d9;padding-bottom:8px;font:500 14px/1.55 "Poppins",sans-serif;color:var(--ink)}
.service-head svg{flex:none}
.service h4{margin-top:16px;font:500 14px "Roboto",sans-serif;color:var(--green)}
.service p{margin-top:12px;height:92px;font:13.5px/1.65 "Roboto",sans-serif;color:#8a8a8a}
.service .btn{margin-top:24px;width:137px;height:38px;font:500 15px "Roboto",sans-serif}
.bars{left:552px;top:1936px;display:flex;gap:8px}
.bars span{width:27px;height:7px;background:#d0d0d0}
.bars span.on{background:var(--green)}

/* reviews */
.review-box{left:112px;top:2250px;width:976px;height:300px;background:var(--green)}
.review-fold{left:112px;top:2520px;width:976px;height:30px;background:#9fa3a0;clip-path:polygon(0 100%,100% 0,100% 100%)}
.review-photo{left:201px;top:2217px;width:120px;height:108px;background:#fff;padding:4px;box-shadow:0 2px 6px rgba(0,0,0,.2)}
.review-photo div{width:100%;height:100%;background:linear-gradient(180deg,#8d8174,#d8d4cf)}
.review-text{left:175px;top:2354px;width:850px;text-align:center;color:#fff;font:15px/1.6 "Tinos",serif}
.qmark{color:#fff;font:700 40px "Tinos",serif}
.review-name{left:0;width:1200px;top:2462px;text-align:center;color:#fff;font:25px "Tinos",serif}

/* contact */
.contact-bg{left:0;top:2916px;width:1200px;height:172px;background:linear-gradient(180deg,#ffffff,#d6d6d6)}
.field{height:59px;border:1.5px solid #bdbdbd;border-radius:4px;background:#fff;box-shadow:0 3px 6px rgba(0,0,0,.08);padding-left:25px;display:flex;align-items:center;font:15px "Poppins",sans-serif;color:#333}
.submit{left:531px;top:2948px;width:138px;height:46px;font:600 16px "Tinos",serif;letter-spacing:.5px}

/* footer */
.footer{left:0;top:3088px;width:1200px;height:317px;background:var(--footer)}
.footer-brand{left:507px;top:3122px;display:flex;align-items:center;gap:8px;color:#fff;font:600 13px/1.3 "Poppins",sans-serif}
.footer-brand .brand-mark{width:52px;height:52px;border-color:#fff;border-width:4px}
.footer-nav{left:0;width:1200px;top:3202px;display:flex;justify-content:center;gap:34px;color:#fff;font:500 15px "Roboto",sans-serif}
.info{top:3262px;display:flex;gap:22px}
.info-ico{width:44px;height:44px;border-radius:50%;background:#4a4a4a;display:flex;align-items:center;justify-content:center;flex:none;margin-top:10px}
.info h5{font:400 25px "Poppins",sans-serif;color:#fff}
.info p{font:14px/1.8 "Poppins",sans-serif;color:#e6e6e6;margin-top:6px}
.divider{top:3255px;width:1px;height:130px;background:#3a3a3a}
.copyright{left:0;width:1200px;top:3424px;text-align:center;font:13px "Poppins",sans-serif;color:#222}
</style>
</head>
<body>

<header>
  <div class="abs topbar"></div>
  <div class="abs topbar-item" style="left:434px">
    <span class="ico"><svg width="13" height="13" viewBox="0 0 24 24"><path fill="#fff" d="M6.6 10.8a15.1 15.1 0 0 0 6.6 6.6l2.2-2.2c.3-.3.7-.4 1-.2 1.1.4 2.3.6 3.6.6.6 0 1 .4 1 1V20c0 .6-.4 1-1 1A17 17 0 0 1 3 4c0-.6.4-1 1-1h3.5c.6 0 1 .4 1 1 0 1.3.2 2.5.6 3.6.1.3 0 .7-.2 1z"/></svg></span>(+612) 9000 4127
  </div>
  <div class="abs topbar-item" style="left:661px">
    <span class="ico"><svg width="13" height="10" viewBox="0 0 22 16"><rect width="22" height="16" rx="2" fill="#fff"/><path d="M1 1l10 7 10-7" stroke="#9a9a9a" stroke-width="2" fill="none"/></svg></span>claire@morlewy.com.au
  </div>
  <div class="abs quote-btn">REQUEST FOR QUOTE</div>
  <div class="abs brand"><span class="brand-mark"></span><span>Quillomette Morlewy<br>Solicitors</span></div>
  <nav class="abs nav"><span>Home</span><span>About us</span><span>Our services</span><span>Contact Us</span><span>Links</span></nav>
  <div class="abs lang"><span class="flag"></span><svg width="9" height="6" viewBox="0 0 9 6"><path d="M1 1l3.5 3.5L8 1" stroke="#999" fill="none"/></svg>Eng</div>
</header>

<section>
  <div class="abs hero" role="img" aria-label="Harbour bridge and city skyline at dusk"></div>
  <div class="abs hero-band"></div>
  <h1 class="abs hero-title">Welcome To<br>Quillomette Morlewy</h1>
  <p class="abs hero-text">Lorem ipsum dolor sit amet, consectetur adipiscing elit, sed do eiusmod tempor incididunt ut labore et dolore magna aliqua.<br>Ut enim ad minim veniam, quis nostrud exercitation ullamco laboris nisi ut aliquip ex ea commodo consequat.</p>
  <div class="abs btn hero-btn">BOOK A CONSULTATION</div>
  <div class="abs dots"><span></span><span class="off"></span><span></span></div>
</section>

<section>
  <div class="abs about-deco"></div>
  <div class="abs about-ring"></div>
  <div class="abs about-photo" role="img" aria-label="Hands signing a legal document beside scales of justice"></div>
  <div class="abs about-portrait" role="img" aria-label="Portrait of the firm's principal solicitor"></div>
  <div class="abs about-body">
    <h2>About Us</h2>
    <p>Claire Morlewy is the principal of the firm. She studied Arts/Law with Honours in French at Harbourside University and commenced work as a Solicitor with the firm Quillomette in 1992. Claire has extensive experience in the following areas:</p>
    <ul>
      <li>Property transactions including the sale and purchase of real estate and commercial leases.</li>
      <li>Sales and purchases of businesses.</li>
      <li>Estates and Wills.</li>
    </ul>
    <p>Claire's first language is English. However, having commenced French lessons at the age of 5 and having lived in France .</p>
    <div class="btn about-btn">LEARN MORE</div>
  </div>
</section>

<section>
  <div class="abs services"></div>
  <div class="abs services-band"></div>
  <div class="abs eyebrow" style="top:1507px">OUR SERVICES</div>
  <h2 class="abs section-title" style="top:1540px">PRACTICE AREAS</h2>

  <div class="abs service" style="left:105px">
    <div class="service-head"><svg width="44" height="44" viewBox="0 0 46 46"><rect x="8" y="4" width="30" height="38" fill="none" stroke="#43624f" stroke-width="3"/><path d="M14 18l9-7 9 7v8H14z" fill="#43624f"/><path d="M14 32h18M14 37h18" stroke="#43624f" stroke-width="2"/></svg><span>Property Law including Conveyancing &amp; Leases</span></div>
    <h4>Buying and selling property</h4>
    <p>Our Property Law team has the legal knowledge and experience to make your purchase or sale of real estate as smooth as possible.</p>
    <div class="btn">Read More</div>
  </div>
  <div class="abs service" style="left:356px">
    <div class="service-head"><svg width="44" height="44" viewBox="0 0 46 46"><circle cx="29" cy="14" r="10" fill="#43624f"/><text x="29" y="19" text-anchor="middle" fill="#fff" font-size="13" font-family="Roboto">$</text><path d="M4 30h8v12H4zM12 32c8-4 12 0 18 0l10-5v5l-12 9H12z" fill="#43624f"/></svg><span>Purchase &amp; Sale of<br>Business</span></div>
    <h4>Buying a Business</h4>
    <p>If you are buying a business, it is important to contact us prior to entering into a legally binding contract.</p>
    <div class="btn">Read More</div>
  </div>
  <div class="abs service" style="left:605px">
    <div class="service-head"><svg width="44" height="44" viewBox="0 0 46 46"><path d="M23 3L4 19h5v10h28V19h5z" fill="#43624f"/><path d="M6 34c8-4 12 0 18 0l12-5v5l-14 9H6z" fill="#43624f"/></svg><span>Wills &amp; Deceased<br>Estates</span></div>
    <h4>Estate Planning</h4>
    <p>Estate Planning involves making a plan for dealing with your assets and debts should something happen to you.</p>
    <div class="btn">Read More</div>
  </div>
  <div class="abs service" style="left:855px">
    <div class="service-head"><svg width="44" height="44" viewBox="0 0 46 46"><rect x="3" y="6" width="40" height="26" fill="#43624f"/><path d="M20 32h6v6h8v3H12v-3h8z" fill="#43624f"/><text x="23" y="24" text-anchor="middle" fill="#fff" font-size="11" font-family="Roboto">A › Z</text></svg><span>Translation &amp; Interpreting Service</span></div>
    <h4>Translation Services</h4>
    <p>we are lawyers and are familiar with English and French legal terms, our legal translations are extremely accurate.</p>
    <div class="btn">Read More</div>
  </div>
  <div class="abs bars"><span class="on"></span><span></span><span></span></div>
</section>

<section>
  <div class="abs eyebrow" style="top:2112px">REVIEWS</div>
  <h2 class="abs section-title" style="top:2152px;color:#111">WHAT OUR CLIENTS SAY</h2>
  <div class="abs review-box"></div>
  <div class="abs review-fold"></div>
  <div class="abs review-photo"><div role="img" aria-label="Client portrait at a desk"></div></div>
  <div class="abs qmark" style="left:140px;top:2328px">&ldquo;</div>
  <p class="abs review-text">Lorem ipsum dolor sit amet, consectetur adipiscing elit, sed do eiusmod tempor incididunt ut labore et dolore magna aliqua. Ut enim ad minim veniam, quis nostrud exercitation ullamco laboris nisi ut aliquip ex ea commodo consequat. Duis aute irure dolor in reprehenderit in voluptate velit esse cillum dolore eu fugiat nulla pariatur. Lorem ipsum dolor sit amet, consectetur adipiscing elit, sed do eiusmod tempor incididunt ut labore et dolore magna aliqua.</p>
  <div class="abs qmark" style="left:932px;top:2426px">&rdquo;</div>
  <div class="abs review-name">Tom Avery</div>
</section>

<section>
  <div class="abs eyebrow" style="top:2614px">CONTACT US</div>
  <h2 class="abs section-title" style="top:2648px;color:#1d3340">SCHEDULE A CONSULTATION</h2>
  <div class="abs contact-bg" role="img" aria-label="City skyline silhouette with harbour landmarks"></div>
  <div class="abs field" style="left:179px;top:2707px;width:411px">First Name *</div>
  <div class="abs field" style="left:610px;top:2707px;width:412px">Last Name *</div>
  <div class="abs field" style="left:179px;top:2781px;width:411px">Email *</div>
  <div class="abs field" style="left:610px;top:2781px;width:412px">Phone</div>
  <div class="abs field" style="left:179px;top:2859px;width:843px">Message</div>
  <div class="abs btn submit">SUBMIT</div>
</section>

<footer>
  <div class="abs footer"></div>
  <div class="abs footer-brand"><span class="brand-mark"></span><span>Quillomette Morlewy<br>Solicitors</span></div>
  <nav class="abs footer-nav"><span>Home</span><span>About Us</span><span>Our services</span><span>Contact Us</span><span>Links</span></nav>
  <div class="abs info" style="left:135px">
    <span class="info-ico"><svg width="18" height="22" viewBox="0 0 18 22"><path d="M9 0a8 8 0 0 0-8 8c0 6 8 14 8 14s8-8 8-14a8 8 0 0 0-8-8z" fill="#fff"/><circle cx="9" cy="8" r="3" fill="#4a4a4a"/></svg></span>
    <div><h5>Address:</h5><p>Level 9, 48 Wattlebrook Lane<br>Sydney, NSW 2000,Australia</p></div>
  </div>
  <div class="abs divider" style="left:438px"></div>
  <div class="abs info" style="left:470px">
    <span class="info-ico"><svg width="20" height="20" viewBox="0 0 24 24"><path fill="#fff" d="M6.6 10.8a15.1 15.1 0 0 0 6.6 6.6l2.2-2.2c.3-.3.7-.4 1-.2 1.1.4 2.3.6 3.6.6.6 0 1 .4 1 1V20c0 .6-.4 1-1 1A17 17 0 0 1 3 4c0-.6.4-1 1-1h3.5c.6 0 1 .4 1 1 0 1.3.2 2.5.6 3.6.1.3 0 .7-.2 1z"/></svg></span>
    <div><h5>Phone Number:</h5><p>(+612) 9000 4127</p></div>
  </div>
  <div class="abs divider" style="left:776px"></div>
  <div class="abs info" style="left:813px">
    <span class="info-ico"><svg width="22" height="16" viewBox="0 0 22 16"><rect width="22" height="16" rx="2" fill="#fff"/><path d="M1 1l10 7 10-7" stroke="#4a4a4a" stroke-width="2" fill="none"/></svg></span>
    <div><h5>Email Address</h5><p>claire@morlewy.com.au</p></div>
  </div>
  <div class="abs copyright">© 2023 <b>Quillomette Morlewy</b> | All Rights Reserved</div>
</footer>

</body>
</html>
```